Letterhead - Pelvarosi Law Group

I receive a fantastic logo from you guys and I'd like to incorporate it into business cards and letterhead. I accidentally approved design No. 58027913 and contacted designer Tarveck, and Tarveck sent me the zip folder for Design No. 58027986, which I very much appreciate.
I'd like to order business cards and letterhead with Design No. 58027986 as soon as possible, but I want to make sure that you incorporate the correct design (attached). I'd also like to provide my information to add (address, phone number, email, fax) but I'm not quite sure how to do it.
The information that I would like on the business cards and letterhead is as follows:
Pelvarosi Law Group
Dorian K. Pelvarosi, Esq.
2741 Halvern Street, Suite 306
San Francisco, CA 94019
Office: (415) 738-0461
Fax: (415) 386-7710
dory@pelvarosilawgroup.com
Thanks in advance for any guidance.
Dory Pelvarosi
Pelvarosi Law Group
(415) 574-8839 (cell)

```html
<!DOCTYPE html>
<html lang="en">
<head>
<meta charset="utf-8">
<title>Pelvarosi Law Group — Stationery</title>
<link href="https://fonts.googleapis.com/css2?family=Open+Sans:wght@400;600;700&display=swap" rel="stylesheet">
<style>
  :root {
    --bg: #3b3b3d;
    --paper: #e4e4e4;
    --paper-light: #ebebeb;
    --grey-mid: #c6c6c6;
    --grey-soft: #b4b4b4;
    --ink: #1a1a1a;
    --black: #161616;
    --charcoal: #3a3a3a;
    --blue: #0b79b3;
    --white: #f4f4f4;
  }
  * { margin: 0; padding: 0; box-sizing: border-box; }
  html, body { width: 1200px; height: 800px; overflow: hidden; }
  body {
    background: var(--bg);
    font-family: "Open Sans", Arial, sans-serif;
    color: var(--ink);
    position: relative;
  }

  /* Business card — front */
  .card { position: absolute; width: 300px; height: 171px; overflow: hidden; }
  .card-front { left: 150px; top: 150px; background: var(--paper-light); }
  .card-front .name {
    position: absolute; left: 16px; top: 14px;
    font-size: 8.5px; font-weight: 700; color: var(--blue); text-transform: uppercase;
  }
  .card-front .role { position: absolute; left: 16px; top: 28px; font-size: 7px; }
  .card-contacts {
    position: absolute; left: 16px; top: 62px; width: 275px;
    display: grid; grid-template-columns: 1fr 1fr; column-gap: 12px; row-gap: 6px;
    font-size: 6.5px; line-height: 1.2;
  }
  .card-contacts li { list-style: none; display: flex; align-items: center; gap: 6px; }
  .card-stripe { position: absolute; left: 0; bottom: 0; width: 300px; height: 42px; }

  /* Business card — back */
  .card-back {
    left: 150px; top: 380px; background: var(--black);
    display: flex; align-items: center; justify-content: center;
  }
  .card-back .wordmark { font-size: 19px; font-weight: 600; color: var(--white); letter-spacing: 0.5px; }

  /* Small icon squares */
  .icon { flex: none; display: inline-flex; align-items: center; justify-content: center; background: var(--blue); }
  .icon svg { display: block; }
  .icon-sm { width: 9px; height: 9px; }
  .icon-md { width: 17px; height: 17px; }

  /* Letterhead */
  .letterhead {
    position: absolute; left: 590px; top: 25px; width: 530px; height: 750px;
    background: var(--paper); overflow: hidden;
  }
  .lh-header { position: absolute; left: 0; top: 0; width: 530px; height: 178px; }
  .lh-header svg.bg { position: absolute; inset: 0; }
  .lh-header .wordmark {
    position: absolute; left: 14px; top: 70px; width: 150px;
    font-size: 19px; line-height: 1.15; font-weight: 600; color: var(--white);
  }
  .lh-contacts {
    position: absolute; right: 14px; top: 36px;
    display: flex; flex-direction: column; align-items: flex-end; gap: 9px;
    font-size: 8px; color: var(--ink);
  }
  .lh-contacts li { list-style: none; display: flex; align-items: center; gap: 6px; text-align: right; line-height: 1.3; }
  .lh-body { position: absolute; left: 13px; top: 192px; width: 506px; font-size: 8.4px; line-height: 1.78; }
  .lh-body .salutation { font-weight: 700; font-size: 8.4px; margin-bottom: 12px; }
  .lh-body p { text-align: justify; margin-bottom: 13px; }
  .signature { position: absolute; right: 27px; top: 640px; width: 115px; border-top: 1px solid var(--ink); text-align: center; padding-top: 5px; font-size: 8px; font-style: italic; }
  .lh-footer { position: absolute; left: 0; bottom: 0; width: 530px; height: 70px; }
</style>
</head>
<body>

<section class="card card-front">
  <h1 class="name">Dorian K. Pelvarosi, Esq.</h1>
  <p class="role">Lawyer</p>
  <ul class="card-contacts">
    <li><span class="icon icon-sm"><svg width="6" height="6" viewBox="0 0 10 10"><path d="M2 1l2 2-1 1.5c.7 1.2 1.3 1.8 2.5 2.5L7 6l2 2-1.5 1.5C4 9 1 6 .5 2.5z" fill="#fff"/></svg></span>(415) 574-8839</li>
    <li><span class="icon icon-sm"><svg width="6" height="6" viewBox="0 0 10 10"><rect x="2.5" y="1" width="5" height="3" fill="#fff"/><rect x="1" y="4" width="8" height="4" fill="#fff"/></svg></span>(415) 386-7710</li>
    <li><span class="icon icon-sm"><svg width="6" height="6" viewBox="0 0 10 10"><path d="M2 1l2 2-1 1.5c.7 1.2 1.3 1.8 2.5 2.5L7 6l2 2-1.5 1.5C4 9 1 6 .5 2.5z" fill="#fff"/></svg></span>(415) 738-0461</li>
    <li><span class="icon icon-sm"><svg width="6" height="6" viewBox="0 0 10 10"><rect x="1" y="2" width="8" height="6" fill="#fff"/><path d="M1 2l4 3 4-3" stroke="#0b79b3" fill="none"/></svg></span>dory@pelvarosilawgroup.com</li>
    <li><span class="icon icon-sm"><svg width="6" height="6" viewBox="0 0 10 10"><circle cx="5" cy="5" r="4" stroke="#fff" fill="none"/><path d="M1 5h8M5 1v8" stroke="#fff"/></svg></span>www.pelvarosilawgroup.com</li>
    <li><span class="icon icon-sm"><svg width="6" height="6" viewBox="0 0 10 10"><path d="M5 .5a3.5 3.5 0 0 1 3.5 3.5C8.5 6.5 5 9.5 5 9.5S1.5 6.5 1.5 4A3.5 3.5 0 0 1 5 .5z" fill="#fff"/></svg></span><span>2741 Halvern Street, Suite 306<br>San Francisco, CA 94019</span></li>
  </ul>
  <svg class="card-stripe" viewBox="0 0 300 42" preserveAspectRatio="none">
    <polygon points="0,0 40,0 62,42 0,42" fill="var(--grey-mid)"/>
    <polygon points="40,14 260,14 272,28 52,28" fill="var(--blue)"/>
    <polygon points="235,0 300,0 300,42 265,42 258,28 272,28" fill="var(--black)"/>
    <polygon points="52,28 258,28 265,42 60,42" fill="var(--paper-light)"/>
  </svg>
</section>

<section class="card card-back">
  <p class="wordmark">Pelvarosi Law Group</p>
</section>

<article class="letterhead">
  <header class="lh-header">
    <svg class="bg" width="530" height="178" viewBox="0 0 530 178">
      <rect width="530" height="178" fill="var(--paper)"/>
      <polygon points="270,0 530,0 530,178 400,178 298,40" fill="var(--grey-mid)"/>
      <polygon points="244,40 270,0 298,40" fill="var(--grey-soft)"/>
      <polygon points="0,0 142,0 255,178 0,178" fill="var(--black)"/>
      <polygon points="142,40 298,40 364,137 204,137" fill="var(--blue)"/>
      <polygon points="204,137 255,137 228,178" fill="var(--charcoal)"/>
    </svg>
    <p class="wordmark">Pelvarosi Law Group</p>
    <ul class="lh-contacts">
      <li>(415) 738-0461<span class="icon icon-md"><svg width="10" height="10" viewBox="0 0 10 10"><path d="M2 1l2 2-1 1.5c.7 1.2 1.3 1.8 2.5 2.5L7 6l2 2-1.5 1.5C4 9 1 6 .5 2.5z" fill="#fff"/></svg></span></li>
      <li>(415) 386-7710<span class="icon icon-md"><svg width="10" height="10" viewBox="0 0 10 10"><rect x="2.5" y="1" width="5" height="3" fill="#fff"/><rect x="1" y="4" width="8" height="4" fill="#fff"/></svg></span></li>
      <li>dory@pelvarosilawgroup.com<span class="icon icon-md"><svg width="10" height="10" viewBox="0 0 10 10"><rect x="1" y="2" width="8" height="6" fill="#fff"/><path d="M1 2l4 3 4-3" stroke="#0b79b3" fill="none"/></svg></span></li>
      <li>www.pelvarosilawgroup.com<span class="icon icon-md"><svg width="10" height="10" viewBox="0 0 10 10"><circle cx="5" cy="5" r="4" stroke="#fff" fill="none"/><path d="M1 5h8M5 1v8" stroke="#fff"/></svg></span></li>
      <li><span>2741 Halvern Street, Suite 306<br>San Francisco, CA 94019</span><span class="icon icon-md"><svg width="10" height="10" viewBox="0 0 10 10"><path d="M5 .5a3.5 3.5 0 0 1 3.5 3.5C8.5 6.5 5 9.5 5 9.5S1.5 6.5 1.5 4A3.5 3.5 0 0 1 5 .5z" fill="#fff"/><circle cx="5" cy="4" r="1.3" fill="#0b79b3"/></svg></span></li>
    </ul>
  </header>

  <main class="lh-body">
    <p class="salutation">DEAR SIR,</p>
    <p>Lorem Ipsum is simply dummy text of the printing and typesetting industry. Lorem Ipsum has been the industry's standard dummy text ever since the 1500s, when an unknown printer took a galley of type and scrambled it to make a type specimen book. It has survived not only five centuries, but also the leap into electronic typesetting, remaining essentially unchanged.</p>
    <p>It was popularised in the 1960s with the release of Pressline sheets containing Lorem Ipsum passages, and more recently with desktop publishing software like Corvell PageSetter including versions of Lorem Ipsum.</p>
    <p>It is a long established fact that a reader will be distracted by the readable content of a page when looking at its layout. The point of using Lorem Ipsum is that it has a more or less normal distribution of letters, as opposed to using 'Content here, content here', making it look like readable English. Many desktop publishing packages and web page editors now use Lorem Ipsum as their default model text, and a search for 'lorem ipsum' will uncover many web sites still in their infancy. If you are going to use a passage of Lorem Ipsum, you need to be sure there isn't anything embarrassing hidden in the middle of text.</p>
  </main>

  <p class="signature">SIGNATURE</p>

  <footer class="lh-footer">
    <svg width="530" height="70" viewBox="0 0 530 70">
      <polygon points="0,0 62,0 124,70 0,70" fill="var(--grey-mid)"/>
      <polygon points="76,28 465,28 480,54 98,54" fill="var(--blue)"/>
      <polygon points="425,0 530,0 530,70 492,70" fill="var(--black)"/>
      <polygon points="425,0 440,0 410,28 405,28" fill="var(--charcoal)"/>
    </svg>
  </footer>
</article>

</body>
</html>
```